GPS business card

Brantor Works is the name of my company
Navs that slot right in!

My Business is supply and install of IN DASH GPS SYSTEMS.
Small family based business that is mobile.

GPS touch screens that are built into the dash.
I have a logo I want Utilized
Wanting colours too

I have screens for all makes and models of vehicles.

I have attached a current business card and some photo's of the work I do.

Target Market(s)

new and used car buyers

Industry/Entity Type

Business

Requirements
Must have
• Name: Ross Brantor

Mob: 0438 512 604
email: rossbrantor@mailvale.net

Must use logo

```html
<!DOCTYPE html>
<html lang="en">
<head>
<meta charset="utf-8">
<title>Brantor Works – Business Cards</title>
<link rel="stylesheet" href="https://fonts.googleapis.com/css2?family=Ubuntu:wght@700&family=Open+Sans:wght@300;400&display=swap">
<style>
  :root {
    --brand-blue: #1466b4;
    --brand-blue-soft: #9fd3f0;
    --accent-orange: #f39a3a;
    --accent-orange-soft: #fbd3b3;
    --card-frame: #000000;
    --card-paper: #ffffff;
    --canvas: #ffffff;
  }
  html, body {
    margin: 0;
    padding: 0;
    width: 1200px;
    height: 1000px;
    overflow: hidden;
    background: var(--canvas);
  }
  .canvas {
    position: relative;
    width: 1200px;
    height: 1000px;
  }
  .card {
    position: absolute;
    top: 352px;
    width: 529px;
    height: 247px;
    box-sizing: border-box;
    border: 9px solid var(--card-frame);
    background: var(--card-paper);
    overflow: hidden;
  }
  .card--swoosh { left: 45px; }
  .card--screen { left: 636px; }

  .brand {
    position: absolute;
    left: 12px;
    top: 12px;
    display: flex;
    align-items: center;
    gap: 14px;
  }
  .brand__mark {
    width: 92px;
    height: 78px;
    background: var(--brand-blue);
    border-radius: 4px;
  }
  .brand__name {
    font-family: "Ubuntu", sans-serif;
    font-weight: 700;
    font-size: 38px;
    line-height: 40px;
    color: var(--brand-blue);
    margin: 0;
  }

  .backdrop {
    position: absolute;
    display: block;
  }
  .backdrop--swoosh {
    left: 150px;
    top: 92px;
    width: 370px;
    height: 150px;
  }
  .backdrop--screen {
    left: 270px;
    top: 25px;
    width: 250px;
    height: 220px;
  }

  .contact {
    position: absolute;
  }
  .card--swoosh .contact { right: 14px; top: 130px; }
  .card--screen .contact { left: 35px; top: 126px; }
  .contact__name {
    margin: 0 0 4px;
    font-family: "Ubuntu", sans-serif;
    font-weight: 700;
    font-size: 37px;
    line-height: 44px;
    color: var(--brand-blue);
    white-space: nowrap;
  }
  .contact__line {
    margin: 0;
    font-family: "Open Sans", sans-serif;
    font-weight: 300;
    font-size: 16px;
    line-height: 23px;
    color: var(--accent-orange);
    white-space: nowrap;
  }
</style>
</head>
<body>
<main class="canvas">

  <section class="card card--swoosh">
    <svg class="backdrop backdrop--swoosh" viewBox="0 0 370 150" role="img" aria-label="Faint orange brand decoration">
      <defs>
        <radialGradient id="swoosh-glow" cx="0.6" cy="0.6" r="0.6">
          <stop offset="0" stop-color="#fbd3b3" stop-opacity="0.55"/>
          <stop offset="1" stop-color="#fbd3b3" stop-opacity="0"/>
        </radialGradient>
      </defs>
      <rect width="370" height="150" fill="url(#swoosh-glow)"/>
    </svg>
    <div class="brand">
      <div class="brand__mark"></div>
      <p class="brand__name">Brantor<br>Works</p>
    </div>
    <div class="contact">
      <h2 class="contact__name">Ross Brantor</h2>
      <p class="contact__line">E: rossbrantor@mailvale.net</p>
      <p class="contact__line">P: 0438 512 604</p>
    </div>
  </section>

  <section class="card card--screen">
    <svg class="backdrop backdrop--screen" viewBox="0 0 250 220" role="img" aria-label="Faint blue brand decoration">
      <defs>
        <radialGradient id="screen-glow" cx="0.55" cy="0.5" r="0.6">
          <stop offset="0" stop-color="#9fd3f0" stop-opacity="0.7"/>
          <stop offset="0.7" stop-color="#9fd3f0" stop-opacity="0.3"/>
          <stop offset="1" stop-color="#9fd3f0" stop-opacity="0"/>
        </radialGradient>
      </defs>
      <rect width="250" height="220" fill="url(#screen-glow)"/>
    </svg>
    <div class="brand">
      <div class="brand__mark"></div>
      <p class="brand__name">Brantor<br>Works</p>
    </div>
    <div class="contact">
      <h2 class="contact__name">Ross Brantor</h2>
      <p class="contact__line">E: rossbrantor@mailvale.net</p>
      <p class="contact__line">P: 0438 512 604</p>
    </div>
  </section>

</main>
</body>
</html>
```